AUSTRALIA SUPPLEMENT - Protein label design - CREATIVE, FEMININE, UNIQUE

I need help with the design of what will be my line of supplements. (Protein, plant base, collagen , BCAAs, etc)
I'm starting off with protein isolate - with the flavours VANILLA, CHOCOLATE, BOYSENBERRY, HONEYCOMB.
I need help with the design of what the product will look like for my range.
(Great opportunity for further work)

Looking for a unique, elegant, stand out, feminine design, some slight sparkle or something that stands out on a shelf.
With symbols to represent what's in it, raised text. with some quirky cute things on it. (not sure what) Something that captured young womens eyes and easy to understand. things on it that appeals to women such as
LOW CALORIE, GREAT TASTING, GLUTEN FREE, 100 NATURAL, NATURALLY SWEETENED, HIGH PROTEIN.etc and whatever you can think of (open to ideas) but within KMO guidelines.

Mostly just after the look and creativity of what the front will look like. Don't have to worry about the back area.

My market will be for females aged 18-35

I have a activewear line called DORUMEN which will go with this. which I will attach the logo below amongst some other things that match my packaging. (again open to ideas)

I have attached a label of what one will look like( EXAMPLE).
. Among others that look nice But again I want to be different, unique to stand out. I don't want it to look like these. it's just the only ones I found online I liked that suit my market.

Feel free to ask any questions! :)
Updates

Extending time as I want this to be to be what will be on the shelves of many stores. I know that needs time to be able to do a quality job.

Target Market(s)

18-35

Industry/Entity Type

Supplement

Font styles to use
Serif
Script

Colors
f9d9e8
ffffff
fbd3d4
ecf7fb
e4daeb
cfeae6
eea4c8
fdfad7
f59195

Requirements
Must have
• Word - DORUMEN
PROTEIN ISOLATE
FLAVOUR
SYMBOLS

Looking for a unique, elegant, stand out, colour, feminine design, some slight sparkle or something that stands out on a shelf.

IT WILL BE ON A WHITE TUB or CLEAR - Perhaps detail on the lid
Nice to have
• Looking for a unique, elegant, stand out, colour, feminine design, some slight sparkle or something that stands out on a shelf. Something artsy.

will be on a white or clear tub with a white label background (possibly)
Should not have
• I don’t want it dark looking.
Something bright, vibrant, whites, pinks, sparkles (maybe) colours.

I don't want the word activewear on it.

```html
<!DOCTYPE html>
<html lang="en">
<head>
<meta charset="utf-8">
<title>Dorumen Protein Isolate – Vanilla Label</title>
<link rel="stylesheet" href="https://fonts.googleapis.com/css2?family=Marcellus&family=Lato:wght@400&display=swap">
<style>
  :root {
    --backdrop: #ede3db;
    --frame-pink: #f59195;
    --label-white: #ffffff;
    --title-pink: #f08e93;
    --flavour-taupe: #a88d7c;
    --ink: #1e1a1a;
    --rule: #ffffff;
    --pattern-pink: #f9d9e8;
    --pattern-cream: #fdfad7;
    --pattern-mint: #cfeae6;
    --petal: #eea4c8;
    --leaf: #6f5f80;
  }
  html, body {
    margin: 0;
    padding: 0;
    width: 1200px;
    height: 1200px;
    overflow: hidden;
    background: var(--backdrop);
  }
  .label {
    position: relative;
    width: 1200px;
    height: 1200px;
    background: var(--backdrop);
  }
  .label__art {
    position: absolute;
    left: 0;
    top: 0;
    width: 1200px;
    height: 840px;
  }
  .brand-name {
    position: absolute;
    left: 0;
    width: 1200px;
    top: 480px;
    text-align: center;
    font-family: "Marcellus", serif;
    font-size: 92px;
    letter-spacing: 0.08em;
    color: var(--ink);
    line-height: 1;
  }
  .product-type {
    position: absolute;
    left: 0;
    width: 1200px;
    top: 838px;
    text-align: center;
    font-family: "Marcellus", serif;
    font-size: 70px;
    color: var(--title-pink);
    line-height: 1;
    letter-spacing: 0.01em;
  }
  .flavour {
    position: absolute;
    left: 0;
    width: 1200px;
    top: 985px;
    text-align: center;
    font-family: "Marcellus", serif;
    font-size: 92px;
    letter-spacing: 0.36em;
    text-indent: 0.36em;
    color: var(--flavour-taupe);
    line-height: 1;
  }
  .flavour-rule {
    position: absolute;
    left: 340px;
    top: 1098px;
    width: 520px;
    height: 1px;
    background: var(--rule);
  }
  .volume {
    position: absolute;
    left: 0;
    width: 1200px;
    top: 1118px;
    text-align: center;
    font-family: "Lato", sans-serif;
    font-size: 34px;
    color: var(--rule);
    line-height: 1;
  }
</style>
</head>
<body>
<main class="label">
  <svg class="label__art" viewBox="0 0 1200 840" xmlns="http://www.w3.org/2000/svg">
    <defs>
      <radialGradient id="patternTone" cx="50%" cy="55%" r="50%">
        <stop offset="0%" stop-color="var(--pattern-pink)" stop-opacity="0.9"/>
        <stop offset="55%" stop-color="var(--pattern-cream)" stop-opacity="0.6"/>
        <stop offset="80%" stop-color="var(--pattern-mint)" stop-opacity="0.35"/>
        <stop offset="100%" stop-color="var(--pattern-pink)" stop-opacity="0"/>
      </radialGradient>
      <linearGradient id="bouquetTone" x1="0" y1="0" x2="1" y2="1">
        <stop offset="0%" stop-color="var(--petal)"/>
        <stop offset="60%" stop-color="#e9a0a6"/>
        <stop offset="100%" stop-color="var(--leaf)"/>
      </linearGradient>
    </defs>

    <ellipse class="doodle-pattern" cx="600" cy="470" rx="460" ry="380"
             fill="url(#patternTone)" role="img"
             aria-label="Pastel line-drawn pattern of hearts, gift boxes and tiny flowers around the frame"/>

    <path class="name-plaque"
          d="M330 300
             C 400 300 430 270 460 250
             C 500 300 700 300 740 250
             C 770 270 800 300 870 300
             C 880 350 920 380 960 380
             L 960 600
             C 920 600 880 630 870 680
             C 800 680 770 705 740 730
             C 700 690 500 690 460 730
             C 430 705 400 680 330 680
             C 320 630 280 600 240 600
             L 240 380
             C 280 380 320 350 330 300 Z"
          fill="var(--label-white)" stroke="var(--frame-pink)" stroke-width="7" stroke-linejoin="round"/>

    <ellipse class="bouquet" cx="600" cy="210" rx="170" ry="100"
             fill="url(#bouquetTone)" opacity="0.85" role="img"
             aria-label="Watercolour pink daisies with dusky purple leaves crowning the frame"/>
  </svg>

  <div class="brand-name">DORUMEN</div>
  <div class="product-type">PROTEIN ISOLATE</div>
  <div class="flavour">VANILLA</div>
  <div class="flavour-rule"></div>
  <div class="volume">250 ml</div>
</main>
</body>
</html>
```